This book will apply the 12 Steps to gaming addiction, also known as video game addiction. The primary purpose of the book is to provide an effective solution for this new type of addiction. The solution is based on the rich and successful concepts of traditional twelve-step programs like RL.

The title on the cover will be "Nine Doors Past the Glowing Screen" and "by Martin Quorby". A subtitle can be used if it works in your design of "A Practical Path Beyond Compulsive Console Play". Cover will be for a 6" x 9" book approximately 110 pages in length.

Some back cover text including some review quotes and an author bio are in the attached Word doc. There is also an author photo attached for for the back cover.

Requirements
Must have
• For the cover design it could be stylized, or an image, a partial image, or whatever. I am open to suggestions. Think about what would be noticed by a person searching for help with moderating their video game use, or by the parents or loved ones of problem gamers. Something contemporary and eye catching.

```html
<!DOCTYPE html>
<html lang="en">
<head>
<meta charset="utf-8">
<title>Nine Doors Past the Glowing Screen — Cover Spread</title>
<link href="https://fonts.googleapis.com/css2?family=Montserrat:wght@500;600;700;800;900&family=Open+Sans:wght@400;600;700&display=swap" rel="stylesheet">
<style>
  :root{
    --page-bg:#f2f3f7;
    --cover-blue:#3b4c8e;
    --cover-glow:#3566ad;
    --navy-band:#2c2a6c;
    --navy-deep:#26256a;
    --accent-orange:#f26a35;
    --text-white:#ffffff;
    --text-soft:#e6e9f6;
    --frame-line:#5d64b0;
    --art-light:#a9b8e6;
    --art-dark:#2d2b72;
  }
  *{box-sizing:border-box;margin:0;padding:0}
  html,body{width:1200px;height:1200px;overflow:hidden}
  body{background:var(--page-bg);font-family:"Open Sans",sans-serif;color:var(--text-white)}
  .spread{position:absolute;left:40px;top:195px;display:flex;gap:40px}
  .cover{width:540px;height:810px;position:relative;overflow:hidden;
    box-shadow:0 14px 40px rgba(20,25,60,.25)}

  /* Front cover */
  .front{background:radial-gradient(circle at 50% 48%,var(--cover-glow) 0%,var(--cover-blue) 62%);
    display:flex;flex-direction:column;align-items:center;padding-top:62px}
  .title{font-family:"Montserrat",sans-serif;font-weight:900;text-transform:uppercase;
    text-align:center;line-height:1.02;text-shadow:3px 4px 0 rgba(10,12,40,.45)}
  .title-lead{display:block;font-size:60px;letter-spacing:1px}
  .title-mid{display:block;font-size:34px;margin-top:4px}
  .title-accent{display:block;font-size:44px;color:var(--accent-orange);margin-top:2px}
  .subtitle{margin-top:22px;background:var(--navy-band);padding:6px 16px;
    font-family:"Montserrat",sans-serif;font-weight:500;font-size:14.5px;letter-spacing:.3px}
  .cover-art{margin-top:38px;width:380px;height:350px;border-radius:26px;
    background:radial-gradient(circle at 45% 55%,var(--art-light) 0%,#5b6cc0 45%,var(--art-dark) 100%)}
  .author-front{margin-top:34px;font-family:"Montserrat",sans-serif;font-weight:700;font-size:52px;letter-spacing:1px}

  /* Back cover */
  .back{background:linear-gradient(180deg,var(--cover-blue) 0%,#33408a 70%,var(--navy-deep) 100%);
    display:flex;flex-direction:column;font-size:10.5px;line-height:1.38}
  .back-content{padding:28px 34px 0}
  .praise-head{display:inline-block;border:1.5px solid var(--frame-line);border-left:none;border-top:none;
    padding:0 14px 4px 0;font-family:"Montserrat",sans-serif;font-weight:700;font-size:15px;line-height:1.25}
  .review{margin-top:10px}
  .review-quote{color:var(--text-soft)}
  .reviewer-name{margin-top:3px;font-family:"Montserrat",sans-serif;font-weight:700;font-size:11px;text-transform:uppercase}
  .reviewer-role{font-size:11px;letter-spacing:.4px}
  .section-break{margin-top:14px;padding-bottom:4px;border-bottom:1.5px solid var(--frame-line);
    font-family:"Montserrat",sans-serif;font-weight:800;font-size:13.5px;text-transform:uppercase;letter-spacing:.6px}
  .blurb{margin-top:8px;color:var(--text-soft)}
  .author-block{margin-top:auto;background:var(--navy-deep);padding:12px 34px 16px;text-align:center}
  .author-head{font-family:"Montserrat",sans-serif;font-weight:700;font-size:13px;letter-spacing:.6px}
  .author-photo{width:70px;height:82px;border-radius:50%;margin:8px auto 8px;
    background:radial-gradient(circle at 50% 45%,#b89a7c 0%,#6d7a4e 55%,#3c4a2c 100%);border:2px solid var(--text-white)}
  .author-bio{text-align:left;color:var(--text-soft)}
  .author-bio strong{color:var(--text-white);font-family:"Montserrat",sans-serif}
</style>
</head>
<body>
<main class="spread">
  <section class="cover front" aria-label="Front cover">
    <h1 class="title">
      <span class="title-lead">Nine Doors</span>
      <span class="title-mid">Past the</span>
      <span class="title-accent">Glowing Screen</span>
    </h1>
    <p class="subtitle">A Practical Path Beyond Compulsive Console Play</p>
    <div class="cover-art" role="img" aria-label="Flat illustration of two young people using a laptop and a phone, seated on a giant game controller in front of a game screen"></div>
    <p class="author-front">Martin Quorby</p>
  </section>

  <section class="cover back" aria-label="Back cover">
    <div class="back-content">
      <h2 class="praise-head">Praise for Nine Doors<br>Past the Glowing Screen</h2>

      <div class="review">
        <p class="review-quote">“A must-read for anyone who is addicted to or thinks they may have a problem with digital gaming. This eloquent work will also be useful to academics and clinicians exploring potential solutions. The author recognizes the similarities between gaming addiction and other addictions, and logically applies one of the most effective known solutions for addiction - The Twelve Steps.”</p>
        <p class="reviewer-name">Dean Whitlock,</p>
        <p class="reviewer-role">Noted Interventionist and Keynote Speaker</p>
      </div>

      <div class="review">
        <p class="review-quote">“If you suffer from digital gaming addiction, I strongly encourage you to use this book as your road map to get you back to the real world.”</p>
        <p class="reviewer-name">Roland Pierce,</p>
        <p class="reviewer-role">Founder of Feed Signal Weekly</p>
      </div>

      <div class="review">
        <p class="review-quote">“As a high school teacher for 24 years, husband, father, coach, and 12-Step member, I can assure you that this book will transform the life of anyone who is addicted to video games. Well written, easy to understand, and a wonderful tool to provide you with a clear road map to recovery, and this includes the students I have been working with in the classroom for decades.”</p>
        <p class="reviewer-name">Tom Delgado,</p>
        <p class="reviewer-role">High School Teacher</p>
      </div>

      <h3 class="section-break">Break to separate sections</h3>
      <p class="blurb">The rising challenge of Digital Gaming Addiction meets the proven and successful tradition of the Twelve Steps. Gaming is a new and troubling phenomenon that has burst onto the scene with alarming speed. Many people crave the use of games the same way as any other addict. Digital Games are a reward system that have been designed to promote compulsive play. This sophisticated technology clearly feeds on natural addictive tendencies. One of the most effective methods for treating addiction in history, beginning with RL in 1939, the 12 Steps have been used to treat a variety of other addictions, including drugs, sex, eating disorders, and many others. Now in this groundbreaking work they are applied to the complex and evolving contemporary phenomenon of Digital Gaming Addiction.</p>
    </div>

    <div class="author-block">
      <h3 class="author-head">About the Author</h3>
      <div class="author-photo" role="img" aria-label="Author portrait photograph"></div>
      <p class="author-bio"><strong>Martin Quorby</strong> is a Technology Consultant and Writer with many years of professional coding and consulting experience. He also struggled with addiction to drugs and alcohol and is now clean and sober in a Twelve-Step program for over 17 years. This unique combination of 12-Step experience and technology expertise led him to create Nine Doors Past the Glowing Screen.</p>
    </div>
  </section>
</main>
</body>
</html>
```